11 x 17 Orvanthes Quote

Design the following quote in a poster.

"First say to yourself what you would be; then do what you have to do." - Orvanthes

See here for inspiration - https://prints.mornbrekal.com/

Quote

```html
<!DOCTYPE html>
<html lang="en">
<head>
<meta charset="utf-8">
<title>Orvanthes Quote Poster</title>
<link rel="stylesheet" href="https://fonts.googleapis.com/css2?family=Bagel+Fat+One&display=swap">
<style>
  :root {
    --backdrop: #ecebe8;
    --paper: #ffffff;
    --ink: #383c3f;
    --accent: #b9473c;
    --accent-fill: #ffffff;
    --credit: #3a1f24;
  }
  html, body {
    margin: 0;
    padding: 0;
    width: 1170px;
    height: 1200px;
    overflow: hidden;
    background: var(--backdrop);
  }
  .poster {
    position: absolute;
    left: 216px;
    top: 30px;
    width: 738px;
    height: 1140px;
    background: var(--paper);
    box-shadow: 0 2px 10px rgba(0,0,0,0.08);
    font-family: "Bagel Fat One", "Cooper Black", serif;
  }
  .quote-line {
    position: absolute;
    left: 0;
    width: 100%;
    margin: 0;
    text-align: center;
    line-height: 1;
    color: var(--ink);
    white-space: nowrap;
  }
  .quote-line--large { font-size: 56px; }
  .quote-line--accent {
    font-size: 46px;
    color: var(--accent-fill);
    -webkit-text-stroke: 12px var(--accent);
    paint-order: stroke fill;
  }
  .accent-word {
    color: var(--accent-fill);
    -webkit-text-stroke: 12px var(--accent);
    paint-order: stroke fill;
  }
  .line-first   { top: 180px; }
  .line-say     { top: 244px; }
  .line-self    { top: 297px; }
  .line-would-1 { top: 418px; }
  .line-would-2 { top: 476px; }
  .line-then    { top: 592px; }
  .line-what    { top: 697px; }
  .line-have    { top: 756px; }
  .credit {
    position: absolute;
    left: 0;
    width: 100%;
    top: 918px;
    margin: 0;
    text-align: center;
    font-size: 18px;
    color: var(--credit);
  }
</style>
</head>
<body>
  <main class="poster">
    <blockquote class="quote">
      <p class="quote-line quote-line--large line-first">“First</p>
      <p class="quote-line quote-line--large line-say">say</p>
      <p class="quote-line quote-line--large line-self">to yourself</p>
      <p class="quote-line quote-line--accent line-would-1">what you</p>
      <p class="quote-line quote-line--accent line-would-2">would be;</p>
      <p class="quote-line quote-line--large line-then">then do</p>
      <p class="quote-line quote-line--large line-what">what you</p>
      <p class="quote-line quote-line--large line-have">have to <span class="accent-word">do.</span>"</p>
    </blockquote>
    <p class="credit">Orvanthes</p>
  </main>
</body>
</html>
```